Corporate Design für Hausverwalterin und Immobilienvermarktung
Zielgruppe
Hausverwalterin und Immobilienvermarktung
Aufgabenstellung
wir sind im Immobiliensektor unterwegs und das Design soll edel und hochwertig sein

```html
<!DOCTYPE html>
<html lang="de">
<head>
<meta charset="utf-8">
<title>Varnel Immobilien – Visitenkarte</title>
<link href="https://fonts.googleapis.com/css2?family=Cinzel:wght@500&family=Montserrat:wght@700&display=swap" rel="stylesheet">
<style>
  :root {
    --navy: #15293d;
    --gold: #d6b369;
    --white: #ffffff;
    --page: #ffffff;
  }
  html, body {
    margin: 0;
    padding: 0;
    width: 1200px;
    height: 1200px;
    overflow: hidden;
    background: var(--page);
  }
  .card {
    position: absolute;
    left: 219px;
    width: 770px;
    height: 440px;
    background: var(--navy);
    box-shadow: 0 6px 28px rgba(0, 0, 0, 0.28);
    box-sizing: border-box;
  }
  .card--front { top: 128px; }
  .card--back {
    top: 639px;
    display: flex;
    flex-direction: column;
    align-items: center;
    justify-content: center;
    font-family: "Montserrat", Arial, sans-serif;
    font-weight: 700;
    font-size: 17.5px;
    line-height: 21px;
    letter-spacing: 0.02em;
    text-transform: uppercase;
    text-align: center;
    color: var(--white);
    padding-top: 6px;
  }
  .brand-mark {
    position: absolute;
    left: 373px;
    top: 172px;
    width: 24px;
    height: 24px;
    background: var(--gold);
  }
  .brand-name {
    position: absolute;
    left: 0;
    right: 0;
    top: 254px;
    text-align: center;
    font-family: "Cinzel", "Times New Roman", serif;
    font-weight: 500;
    font-size: 31px;
    letter-spacing: 0.02em;
    color: var(--gold);
    margin: 0;
  }
  .brand-tagline {
    position: absolute;
    left: 0;
    right: 0;
    top: 292px;
    text-align: center;
    font-family: "Cinzel", "Times New Roman", serif;
    font-weight: 500;
    font-size: 9.5px;
    letter-spacing: 0.04em;
    color: var(--gold);
    margin: 0;
  }
  .gold { color: var(--gold); }
  .block { margin: 0; }
  .block + .block { margin-top: 20px; }
</style>
</head>
<body>
  <section class="card card--front">
    <span class="brand-mark"></span>
    <h1 class="brand-name">VARNEL IMMOBILIEN</h1>
    <p class="brand-tagline">VERWALTUNG UND VERMARKTUNG</p>
  </section>

  <section class="card card--back">
    <p class="block headline gold">Ganzheitliche Immobilienbetreuung mit Strategie.</p>
    <p class="block intro">Als zertifizierte Hausverwalterin &amp; Immobilienmaklerin<br>gemäß § 34c GewO verbinde ich klassische<br>Verwaltung mit wertoptimierter Vermarktung:</p>
    <p class="block services gold">- Hausverwaltung: rechtssicher &amp; entlastend.<br>- Asset Management: strategische Ertragssteigerung.<br>- Verkauf: marktgerecht &amp; professionell.</p>
    <p class="block contact">Telefon: 0160 381 92 47<br><span class="gold">Varnel Immobilien - Ihr Eigentum in zuverlässigen Händen.</span><br>E-Mail: info@varnel-immobilien.de<br>Webseite: www.varnel-immobilien.de</p>
  </section>
</body>
</html>
```